Swimming Pool Supply Company Business Cards

We need business cards designed for company. These need to be easy to edit so that we can fill in names, titles, and contact info for each person who works here.

Dalton R. Pembry
Manager of Legal & Finance
J.L. Pembry, Incorporated

4837 Grelwood Avenue
Marlow Crossing, PA 19054

E. dalton@jlpembry.com
M. (215) 555-7193
O. (215) 555-4620

Contact Information for Business Card

Looking to upgrade current business cards with graphic that can be edited. Looking for fresh ideas for an age old industry.

Font styles to use
Serif
Sans Serif

Colors

Designer to choose colors to be used in the design.

Requirements
Must have
• Professional, fresh, unique but professional

```html
<!DOCTYPE html>
<html lang="en">
<head>
<meta charset="utf-8">
<title>Pembry Business Card</title>
<link rel="stylesheet" href="https://fonts.googleapis.com/css2?family=Jost:wght@400;500;600;700&display=swap">
<style>
  :root {
    --page: #e8e3da;
    --card: #f7f7f6;
    --ink: #111111;
    --band: #1a1a1a;
    --name: #2e2e2e;
    --muted: #9a9a9a;
    --body: #555555;
    --icon: #333333;
    --shadow: rgba(40, 30, 20, 0.28);
  }
  * { box-sizing: border-box; margin: 0; padding: 0; }
  html, body {
    width: 1200px; height: 950px; overflow: hidden;
    background: var(--page);
    font-family: "Jost", "Helvetica Neue", Arial, sans-serif;
  }
  .canvas { position: relative; width: 1200px; height: 950px; }

  .card {
    position: absolute;
    width: 540px; height: 310px;
    background: var(--card);
    box-shadow: 0 3px 0 #d6d6d6, 0 6px 0 #c9c9c9, 0 14px 28px var(--shadow);
    overflow: hidden;
  }
  .card--front { left: 70px; top: 150px; }
  .card--back  { left: 590px; top: 490px; }

  /* front */
  .brand-band {
    position: absolute; right: 0; top: 0; bottom: 0; width: 120px;
    background: var(--band);
  }
  .brand-band .brand {
    position: absolute; left: 50%; top: 50%;
    transform: translate(-50%, -50%) rotate(-90deg);
    display: flex; flex-direction: column; align-items: center;
    white-space: nowrap; color: #ffffff;
  }
  .brand-name {
    font-weight: 700; letter-spacing: 2px; line-height: 1;
  }
  .brand-band .brand-name { font-size: 52px; }
  .tagline { font-weight: 400; letter-spacing: 0.2px; }
  .brand-band .tagline { font-size: 11px; margin-top: 4px; }

  .contact { position: absolute; left: 40px; top: 42px; right: 150px; }
  .person { display: flex; gap: 12px; align-items: flex-start; }
  .person-name {
    font-size: 22px; font-weight: 600; color: var(--name);
    letter-spacing: 0.5px; text-transform: uppercase; line-height: 1.1;
  }
  .person-role, .person-company {
    font-size: 15px; color: var(--muted); line-height: 1.3;
  }
  .person-role { margin-top: 4px; }

  .detail { display: flex; gap: 12px; margin-top: 20px; }
  .detail-text { font-size: 15px; color: var(--body); line-height: 1.3; }
  .icon-col { display: flex; flex-direction: column; }
  .icon { width: 16px; height: 16px; flex: none; margin-top: 2px; }
  .icon-col .icon { height: 19.5px; margin-top: 0; padding-top: 2px; }

  /* back */
  .card--back .brand {
    position: absolute; left: 50%; top: 50%;
    transform: translate(-50%, -50%);
    display: flex; flex-direction: column; align-items: center;
    color: var(--ink); white-space: nowrap;
  }
  .card--back .brand-name { font-size: 88px; letter-spacing: 3px; }
  .card--back .tagline { font-size: 15px; margin-top: 6px; color: #333333; }
</style>
</head>
<body>
<main class="canvas">

  <article class="card card--front">
    <section class="contact">
      <div class="person">
        <svg class="icon" viewBox="0 0 16 16" aria-hidden="true"><circle cx="8" cy="5" r="3.2" fill="var(--icon)"/><path d="M2 15c0-3.6 2.7-5.6 6-5.6s6 2 6 5.6z" fill="var(--icon)"/></svg>
        <div>
          <h1 class="person-name">Dalton R. Pembry</h1>
          <p class="person-role">Manager of Legal &amp; Finance</p>
          <p class="person-company">J.L. Pembry, Incorporated</p>
        </div>
      </div>

      <div class="detail">
        <svg class="icon" viewBox="0 0 16 16" aria-hidden="true"><path d="M8 1a5 5 0 0 0-5 5c0 3.8 5 9 5 9s5-5.2 5-9a5 5 0 0 0-5-5z" fill="var(--icon)"/><circle cx="8" cy="6" r="1.8" fill="var(--card)"/></svg>
        <p class="detail-text">4837 Grelwood Avenue<br>Marlow Crossing, PA 19054</p>
      </div>

      <div class="detail">
        <div class="icon-col">
          <svg class="icon" viewBox="0 0 16 16" aria-hidden="true"><path d="M3 2l3 0 1 3-2 1.5c.8 1.8 2 3 3.5 3.5L10 8l3 1v3c0 .6-.5 1-1 1C6.5 13 3 9.5 3 4z" fill="var(--icon)"/></svg>
          <svg class="icon" viewBox="0 0 16 16" aria-hidden="true"><rect x="4.5" y="1.5" width="7" height="13" rx="1.2" fill="none" stroke="var(--icon)" stroke-width="1.5"/><circle cx="8" cy="12" r="0.9" fill="var(--icon)"/></svg>
          <svg class="icon" viewBox="0 0 16 16" aria-hidden="true"><rect x="1.5" y="3.5" width="13" height="9" fill="none" stroke="var(--icon)" stroke-width="1.5"/><path d="M1.5 3.5 8 9l6.5-5.5" fill="none" stroke="var(--icon)" stroke-width="1.5"/></svg>
          <svg class="icon" viewBox="0 0 16 16" aria-hidden="true"><circle cx="8" cy="8" r="6.3" fill="none" stroke="var(--icon)" stroke-width="1.4"/><ellipse cx="8" cy="8" rx="2.6" ry="6.3" fill="none" stroke="var(--icon)" stroke-width="1.2"/><path d="M1.7 8h12.6" stroke="var(--icon)" stroke-width="1.2"/></svg>
        </div>
        <p class="detail-text">(215) 555-4620<br>(215) 555-7193<br>dalton@jlpembry.com<br>www.jlpembry.com</p>
      </div>
    </section>

    <aside class="brand-band">
      <div class="brand">
        <span class="brand-name">PEMBRY</span>
        <span class="tagline">Big Enough to Serve You, Small Enough to Care</span>
      </div>
    </aside>
  </article>

  <article class="card card--back">
    <div class="brand">
      <span class="brand-name">PEMBRY</span>
      <span class="tagline">Big Enough to Serve You, Small Enough to Care</span>
    </div>
  </article>

</main>
</body>
</html>
```